Letterhead design for Dental Practice - Ashby Lane Dental Care

Letterhead for Private Dental Practice. To be used for all official correspondance and for printing treatment details on to be given to patients.

Target Market(s)

Private dental patients

Industry/Entity Type

Dental Clinic

Font styles to use
Other font styles liked:
• nexa-light

Colors
33a6d7
1c66ac
85abd2

Requirements
Must have
• info in the footer and header needs to be 3.5cm from upper/lower boader of paper, see photo in uploaded files
• info details:
• tel. 0115 947 3051
• email info@ashbylanedc.co.uk
• ashbylanedentalcare.co.uk
• 17b Ashby Lane West Bridgford Nottingham NG2 7QT
• nexa-light font as in uploaded logo files
Should not have
• No funny tooth pictures

```html
<!DOCTYPE html>
<html lang="en">
<head>
<meta charset="utf-8">
<title>Ashby Lane Dental Care – Letterhead</title>
<link rel="stylesheet" href="https://fonts.googleapis.com/css2?family=Montserrat:wght@300&family=Source+Sans+3:wght@400&display=swap">
<style>
  :root {
    --brand-blue: #1a9ddb;
    --swoosh-grey: #555659;
    --paper: #fafafa;
    --backdrop: #e4e5e6;
    --ink: #3a3a3a;
    --ink-strong: #111111;
    --footer-text: #ffffff;
    --signature-tone: #d9d9d9;
  }
  * { box-sizing: border-box; margin: 0; padding: 0; }
  html, body {
    width: 1200px; height: 998px; overflow: hidden;
    background: var(--backdrop);
  }
  .letterhead {
    position: absolute; left: 260px; top: 19px;
    width: 680px; height: 960px;
    background: var(--paper);
    overflow: hidden;
  }
  .letterhead__bands {
    position: absolute; inset: 0; width: 680px; height: 960px;
  }
  .brand {
    position: absolute; top: 82px; left: 0; width: 680px;
    display: flex; justify-content: center; align-items: center; gap: 10px;
  }
  .brand__dot {
    width: 14px; height: 14px; border-radius: 50%;
    background: var(--brand-blue);
  }
  .brand__name {
    font-family: "Montserrat", sans-serif; font-weight: 300;
    font-size: 24px; color: var(--brand-blue); letter-spacing: 0.5px;
  }
  .letter {
    position: absolute; left: 43px; top: 200px; width: 593px;
    font-family: "Source Sans 3", sans-serif; font-size: 13.4px;
    line-height: 17.8px; color: var(--ink); letter-spacing: -0.15px;
  }
  .letter__salutation {
    font-family: Arial, Helvetica, sans-serif; font-weight: 700;
    font-size: 14.5px; color: var(--ink-strong); margin-bottom: 21px;
  }
  .letter__para { text-align: justify; margin-bottom: 17.8px; }
  .signature {
    position: absolute; left: 43px; top: 765px;
    width: 105px; height: 52px; border-radius: 4px;
    background: var(--signature-tone);
  }
  .contact {
    position: absolute; top: 924px;
    font-family: "Montserrat", sans-serif; font-weight: 300;
    font-size: 10px; line-height: 15px; color: var(--footer-text);
  }
  .contact--left { left: 43px; }
  .contact--left b { font-weight: 300; }
  .contact--centre { left: 0; width: 680px; text-align: center; top: 939px; }
  .contact--right { right: 44px; text-align: right; }
</style>
</head>
<body>
  <div class="letterhead">
    <svg class="letterhead__bands" viewBox="0 0 680 960" aria-hidden="true">
      <path fill="var(--brand-blue)" d="M0 0 H680 V83 Q340 -3 0 83 Z"/>
      <path fill="var(--swoosh-grey)" d="M25 84 Q340 -20 655 84 Q340 0 25 84 Z"/>
      <path fill="var(--brand-blue)" d="M0 870 Q340 962 680 870 V960 H0 Z"/>
      <path fill="var(--swoosh-grey)" d="M25 868 Q340 970 655 868 Q340 950 25 868 Z"/>
    </svg>

    <header class="brand">
      <span class="brand__dot"></span>
      <span class="brand__name">Ashby Lane Dental Care</span>
    </header>

    <main class="letter">
      <p class="letter__salutation">Dear Mr. Hale,</p>
      <p class="letter__para">Lorem Ipsum is simply dummy text of the printing and typesetting industry. Lorem Ipsum has been the industry's standard dummy text ever since the 1500s, when an unknown printer took a galley of type and scrambled it to make a type specimen book. It has survived not only five centuries, but also the leap into electronic typesetting, remaining essentially unchanged.</p>
      <p class="letter__para">The standard chunk of Lorem Ipsum used since the 1500s is reproduced below for those interested. Sections 1.10.32 and 1.10.33 from "de Finibus Bonorum et Malorum" by Cicero are also reproduced in their exact original form, accompanied by English versions from the 1914 translation by H. Rackham</p>
      <p class="letter__para">Lorem Ipsum is simply dummy text of the printing and typesetting industry. Lorem Ipsum has been the industry's standard dummy text ever since the 1500s, when an unknown printer took a galley of type and scrambled it to make a type specimen book. It has survived not only five centuries, but also the leap into electronic typesetting, remaining essentially unchanged. It was popularised in the</p>
      <p class="letter__para">The standard chunk of Lorem Ipsum used since the 1500s is reproduced below for those interested. Sections 1.10.32 and 1.10.33 from "de Finibus Bonorum et Malorum" by Cicero are also reproduced in their exact original form, accompanied by English versions from the 1914 translation by H. Rackham</p>
      <p class="letter__para">The standard chunk of Lorem Ipsum used since the 1500s is reproduced below for those interested. Sections 1.10.32 and 1.10.33 from "de Finibus Bonorum et Malorum" by Cicero are also reproduced in their exact original form.</p>
    </main>

    <div class="signature" role="img" aria-label="Handwritten signature of the sender"></div>

    <footer>
      <div class="contact contact--left">
        <div><b>P:</b> 0115 947 3051</div>
        <div><b>E:</b> info@ashbylanedc.co.uk</div>
      </div>
      <div class="contact contact--centre">www.ashbylanedentalcare.co.uk</div>
      <div class="contact contact--right">
        <div>17b Ashby Lane, West Bridgford,</div>
        <div>Nottingham NG2 7QT</div>
      </div>
    </footer>
  </div>
</body>
</html>
```